Real Estate Design Website

I would like to have a design for "real estate agent" website. It needs to be in a "Responsive" framework.

The design need to be suitable for different viewer from all around the world. It needs to be modern. It'd be great if there is a design for mobile and vexo/tablet (it's all under responsive framework). It needs to be easy to navigate and look modern

Target Market(s)

End user/Real estate buyers from different part of the world

Industry/Entity Type

Real Estate

Requirements
Must have
• It's for real estate agent website which is used to represent their brand/image but at the same time it also for their client which is real estate buyers
Should not have
• Should not be boring design/out of date

```html
<!DOCTYPE html>
<html lang="en">
<head>
<meta charset="utf-8">
<title>Real Estate Agent</title>
<link rel="stylesheet" href="https://fonts.googleapis.com/css2?family=Lato:wght@300;400;700&display=swap">
<style>
:root{
  --brand:#14789f;
  --brand-light:#1c8cc0;
  --ink:#1c1c1c;
  --text:#555;
  --muted:#777;
  --page:#e8e8e8;
  --panel:#ffffff;
  --field:#dcdcdc;
  --black:#0a0a0a;
  --sky-top:#3d87c9;
  --sky-mid:#9ec3e0;
  --city:#7a6a58;
  --water:#2f6b91;
}
*{box-sizing:border-box;margin:0;padding:0}
html,body{width:978px;height:1200px;overflow:hidden}
body{background:var(--page);font-family:"Lato",sans-serif;color:var(--ink);position:relative}
.abs{position:absolute}
.hero-photo{left:0;top:0;width:978px;height:361px;background:linear-gradient(180deg,var(--sky-top) 0%,var(--sky-mid) 32%,var(--city) 62%,var(--water) 100%)}
.column{left:118px;top:320px;width:742px;height:827px;background:var(--panel)}
.header-bar{left:118px;top:0;width:742px;height:49px;background:var(--panel)}
.logo{left:118px;top:0;width:164px;height:49px;background:var(--brand);color:#fff;font-weight:700;font-size:16px;line-height:49px;padding-left:14px;white-space:nowrap;overflow:hidden;letter-spacing:-0.3px}
.nav{right:261px;top:16px;display:flex;gap:15px;font-size:12px;color:#333;white-space:nowrap}
.nav a{color:inherit;text-decoration:none}
.nav .active{color:var(--brand-light);border-bottom:2px solid var(--brand-light);padding-bottom:3px}
.site-search{left:727px;top:16px;width:117px;height:17px;background:var(--black)}
.site-search .btn{position:absolute;right:0;top:0;width:18px;height:17px;background:var(--brand-light)}
.login{left:725px;top:49px;width:135px;height:84px;background:var(--brand)}
.login .field{position:absolute;left:8px;width:118px;height:15px;background:#fff;font-size:10px;color:#555;padding-left:5px;line-height:15px}
.login .remember{position:absolute;left:8px;top:60px;font-size:10px;color:#111;display:flex;align-items:center;gap:3px}
.login .remember i{width:8px;height:8px;background:#fff;display:block}
.btn-row{display:flex;height:100%}
.btn-row .label{flex:1;display:flex;align-items:center;justify-content:center}
.btn-row .arrow{width:28px;background:var(--black);display:flex;align-items:center;justify-content:center}
.login-btn{left:725px;top:133px;width:135px;height:31px;background:#fff;color:var(--brand-light);font-size:17px}
.hero-title{left:333px;top:128px;width:322px;height:55px;background:rgba(120,120,120,.45);text-align:center;color:#fff}
.hero-title h1{font-weight:300;font-size:35px;line-height:36px;letter-spacing:0.5px}
.hero-title p{font-weight:300;font-size:14px;line-height:16px}
.slider-arrows{left:451px;top:269px;display:flex;gap:6px}
.slider-arrows span{width:26px;height:28px;background:var(--black);display:flex;align-items:center;justify-content:center}
.register{left:714px;top:291px;width:146px;height:29px;background:var(--brand);color:#fff;font-size:16px}
.finder{left:118px;top:227px;width:261px;height:134px;background:var(--panel)}
.select{position:absolute;width:116px;height:19px;background:var(--field);font-size:11px;color:#555;line-height:19px;padding-left:6px}
.select i{position:absolute;right:2px;top:2px;width:15px;height:15px;background:var(--black);display:flex;align-items:center;justify-content:center}
.search-btn{left:213px;top:292px;width:70px;height:21px;background:var(--brand);color:#fff;font-size:14px}
.search-btn .arrow{width:20px}
.section-title{left:141px;top:339px;font-weight:300;font-size:25px;color:var(--brand-light)}
.card{width:218px}
.card .photo{width:217px;height:92px}
.card h2{font-weight:400;font-size:15px;margin-top:14px;color:#222}
.card .desc{font-size:10.5px;line-height:15px;color:var(--muted);margin-top:7px;font-weight:300}
.plus{display:inline-flex;width:11px;height:11px;border-radius:50%;background:var(--black);color:#fff;font-size:10px;line-height:11px;justify-content:center;vertical-align:middle;margin-left:5px}
.plus.hover{background:var(--brand-light)}
.features{display:flex;gap:11px;font-size:8.5px;color:#333;margin-top:13px}
.features span{display:flex;align-items:center;gap:4px}
.features svg{width:14px;height:9px}
.divider{left:142px;top:618px;width:690px;height:1px;background:#cfcfcf}
.band{left:118px;top:911px;width:742px;height:134px;background:var(--brand);color:#fff}
.band h3{font-weight:300;font-size:20px;position:absolute;top:17px}
.band p{font-size:11px;line-height:13px;font-weight:300;position:absolute;top:48px}
.band .more-link{font-size:11px;font-weight:300;position:absolute;display:flex;align-items:center}
.band .more-link .plus{background:#fff;color:var(--brand)}
.more-btn{left:766px;top:1045px;width:94px;height:30px;background:var(--brand);color:#fff;font-size:16px}
.more-btn .arrow{color:var(--brand-light);font-size:16px}
.social{left:136px;top:1100px;display:flex;gap:3px}
.social span{width:27px;height:27px;background:var(--black)}
.social span:first-child{background:var(--brand)}
.copyright{left:237px;top:1107px;font-size:10px;color:#333}
.legal{right:118px;top:1165px;display:flex;gap:12px;font-size:10px;color:#555}
</style>
</head>
<body>

<div class="abs hero-photo" role="img" aria-label="Photo of a city skyline of tall towers across a harbour under blue sky"></div>
<div class="abs column"></div>

<header>
  <div class="abs header-bar"></div>
  <div class="abs logo">REAL ESTATE AGENT</div>
  <nav class="abs nav">
    <a class="active">Home</a><a>Find Property</a><a>Offices</a><a>Associates</a><a>Contact</a>
  </nav>
  <div class="abs site-search"><span class="btn">
    <svg width="18" height="17" viewBox="0 0 18 17"><circle cx="8" cy="7.5" r="3.5" fill="none" stroke="#fff" stroke-width="1.5"/><line x1="10.5" y1="10" x2="13" y2="12.5" stroke="#fff" stroke-width="1.5"/></svg>
  </span></div>
</header>

<div class="abs login">
  <div class="field" style="top:14px">username</div>
  <div class="field" style="top:37px">password</div>
  <div class="remember"><i></i>remember me</div>
</div>
<div class="abs login-btn"><div class="btn-row"><span class="label">Login</span><span class="arrow"><svg width="10" height="14" viewBox="0 0 10 14"><polyline points="2,1 8,7 2,13" fill="none" stroke="#fff" stroke-width="1.6"/></svg></span></div></div>

<div class="abs hero-title">
  <h1>NAM QUIS LIGULA</h1>
  <p>A NIBH FERMENTUM VENENATIS</p>
</div>

<div class="abs slider-arrows">
  <span><svg width="10" height="14" viewBox="0 0 10 14"><polyline points="8,1 2,7 8,13" fill="none" stroke="#fff" stroke-width="1.6"/></svg></span>
  <span><svg width="10" height="14" viewBox="0 0 10 14"><polyline points="2,1 8,7 2,13" fill="none" stroke="#fff" stroke-width="1.6"/></svg></span>
</div>

<div class="abs register"><div class="btn-row"><span class="label">Register Now</span><span class="arrow" style="width:35px"><svg width="10" height="14" viewBox="0 0 10 14"><polyline points="2,1 8,7 2,13" fill="none" stroke="#fff" stroke-width="1.6"/></svg></span></div></div>

<div class="abs finder">
  <div class="select" style="left:11px;top:14px">City<i><svg width="9" height="6" viewBox="0 0 9 6"><polygon points="0,0 9,0 4.5,6" fill="#fff"/></svg></i></div>
  <div class="select" style="left:132px;top:14px">Lifestyle<i><svg width="9" height="6" viewBox="0 0 9 6"><polygon points="0,0 9,0 4.5,6" fill="#fff"/></svg></i></div>
  <div class="select" style="left:11px;top:37px">Property type<i><svg width="9" height="6" viewBox="0 0 9 6"><polygon points="0,0 9,0 4.5,6" fill="#fff"/></svg></i></div>
  <div class="select" style="left:132px;top:37px">Price<i><svg width="9" height="6" viewBox="0 0 9 6"><polygon points="0,0 9,0 4.5,6" fill="#fff"/></svg></i></div>
</div>
<div class="abs search-btn"><div class="btn-row"><span class="label">Search</span><span class="arrow"><svg width="8" height="12" viewBox="0 0 8 12"><polyline points="2,1 6,6 2,11" fill="none" stroke="#fff" stroke-width="1.4"/></svg></span></div></div>

<h2 class="abs section-title">Featured Property</h2>

<svg width="0" height="0" style="position:absolute">
  <defs>
    <symbol id="ico-bed" viewBox="0 0 14 9"><rect x="0" y="1" width="2" height="8" fill="#555"/><rect x="0" y="5" width="14" height="2" fill="#555"/><rect x="3" y="3" width="4" height="2" fill="#555"/><rect x="12" y="5" width="2" height="4" fill="#555"/></symbol>
    <symbol id="ico-bath" viewBox="0 0 14 9"><rect x="1" y="4" width="12" height="3" fill="#555"/><rect x="2" y="0" width="2" height="4" fill="#555"/><rect x="3" y="7" width="1.5" height="2" fill="#555"/><rect x="10" y="7" width="1.5" height="2" fill="#555"/></symbol>
    <symbol id="ico-car" viewBox="0 0 14 9"><path d="M1 5 L3 1 H11 L13 5 V8 H1 Z" fill="#555"/><circle cx="4" cy="8" r="1.2" fill="#fff"/><circle cx="10" cy="8" r="1.2" fill="#fff"/></symbol>
  </defs>
</svg>

<article class="abs card" style="left:143px;top:387px">
  <div class="photo" role="img" aria-label="Photo of glass office towers against blue sky" style="background:linear-gradient(160deg,#1f5fb0,#4f86c8 50%,#2a3b55)"></div>
  <h2>Nam quis ligula a nibh</h2>
  <p class="desc">Etiam non felis mi. Quisque feugiat, lectus non feugiat consectetur, purus ipsum lobortis nisl, a sollicitudin risus arcu<span class="plus hover">+</span></p>
  <div class="features"><span><svg><use href="#ico-bed"/></svg>3 Bedrooms</span><span><svg><use href="#ico-bath"/></svg>2 Bathrooms</span><span><svg><use href="#ico-car"/></svg>2 Garages</span></div>
</article>
<article class="abs card" style="left:378px;top:387px">
  <div class="photo" role="img" aria-label="Photo of a white family house with a garden" style="background:linear-gradient(180deg,#b9d3ea,#d9d6cc 45%,#5d7a3a)"></div>
  <h2>Nam quis ligula a nibh</h2>
  <p class="desc">Etiam non felis mi. Quisque feugiat, lectus non feugiat consectetur, purus ipsum lobortis nisl, a sollicitudin risus arcu<span class="plus">+</span></p>
  <div class="features"><span><svg><use href="#ico-bed"/></svg>3 Bedrooms</span><span><svg><use href="#ico-bath"/></svg>2 Bathrooms</span><span><svg><use href="#ico-car"/></svg>2 Garages</span></div>
</article>
<article class="abs card" style="left:613px;top:387px">
  <div class="photo" role="img" aria-label="Photo of a white seaside apartment building" style="background:linear-gradient(180deg,#3a78c8,#a9c4df 40%,#e8e6e0 70%,#6b8a4f)"></div>
  <h2>Nam quis ligula a nibh</h2>
  <p class="desc">Etiam non felis mi. Quisque feugiat, lectus non feugiat consectetur, purus ipsum lobortis nisl, a sollicitudin risus arcu<span class="plus">+</span></p>
  <div class="features"><span><svg><use href="#ico-bed"/></svg>3 Bedrooms</span><span><svg><use href="#ico-bath"/></svg>2 Bathrooms</span><span><svg><use href="#ico-car"/></svg>2 Garages</span></div>
</article>

<div class="abs divider"></div>

<article class="abs card" style="left:143px;top:645px">
  <div class="photo" role="img" aria-label="Photo of a grey two storey house with a porch among trees" style="background:linear-gradient(180deg,#4e6a3a,#8a8f8a 45%,#4a5a32)"></div>
  <h2>Nam quis ligula a nibh</h2>
  <p class="desc">Etiam non felis mi. Quisque feugiat, lectus non feugiat consectetur, purus ipsum lobortis nisl, a sollicitudin risus arcu<span class="plus">+</span></p>
  <div class="features"><span><svg><use href="#ico-bed"/></svg>3 Bedrooms</span><span><svg><use href="#ico-bath"/></svg>2 Bathrooms</span><span><svg><use href="#ico-car"/></svg>2 Garages</span></div>
</article>
<article class="abs card" style="left:378px;top:645px">
  <div class="photo" role="img" aria-label="Photo of a beige suburban house with gables" style="background:linear-gradient(180deg,#3f5c2e,#b3a88e 45%,#50672f)"></div>
  <h2>Nam quis ligula a nibh</h2>
  <p class="desc">Etiam non felis mi. Quisque feugiat, lectus non feugiat consectetur, purus ipsum lobortis nisl, a sollicitudin risus arcu<span class="plus">+</span></p>
  <div class="features"><span><svg><use href="#ico-bed"/></svg>3 Bedrooms</span><span><svg><use href="#ico-bath"/></svg>2 Bathrooms</span><span><svg><use href="#ico-car"/></svg>2 Garages</span></div>
</article>
<article class="abs card" style="left:613px;top:645px">
  <div class="photo" role="img" aria-label="Photo of a stone and siding house with tall windows" style="background:linear-gradient(180deg,#7fa0c4,#8a7865 45%,#5a6b3a)"></div>
  <h2>Nam quis ligula a nibh</h2>
  <p class="desc">Etiam non felis mi. Quisque feugiat, lectus non feugiat consectetur, purus ipsum lobortis nisl, a sollicitudin risus arcu<span class="plus">+</span></p>
  <div class="features"><span><svg><use href="#ico-bed"/></svg>3 Bedrooms</span><span><svg><use href="#ico-bath"/></svg>2 Bathrooms</span><span><svg><use href="#ico-car"/></svg>2 Garages</span></div>
</article>

<section class="abs band">
  <h3 style="left:21px">News</h3>
  <p style="left:21px;width:235px">Mauris vel volutpat leo. Nunc non justo nunc. Donec sapien arcu, egestas at facilisis et, interdum eget mauris.</p>
  <span class="more-link" style="left:21px;top:100px">Read the full story<span class="plus">+</span></span>
  <h3 style="left:263px">What Our Client Say</h3>
  <p style="left:263px;width:470px">Mauris vel volutpat leo. Nunc non justo nunc. Donec sapien arcu, egestas at facilisis et, interdum eget mauris. vitae bibendum mauris. Vestibulum vehicula posuere hendrerit. risus vestibulum auctor. In hac habitasse platea dictumst.</p>
  <span class="more-link" style="left:263px;top:100px">More tesimonials<span class="plus">+</span></span>
</section>

<div class="abs more-btn"><div class="btn-row"><span class="label">More</span><span class="arrow">+</span></div></div>

<div class="abs social" aria-label="Social links"><span></span><span></span><span></span></div>
<p class="abs copyright">Copyright Real Estate Agent 2013.All Rights Reserved.</p>

<nav class="abs legal"><span>Terms</span><span>Privacy</span><span>Contact</span></nav>

</body>
</html>
```